Labour Day banner showcasing 20% off site

Banner graphic promoting our Labour Day sale
Size: 2000px x 600px
- examples from other companies and their sale banners have been uploaded for inspiration. Labour day examples are for the United States's holiday and submissions should NOT be in their country colours.
- product images can be found at www.fernlowleaf.com

Target Market(s)

19+

Industry/Entity Type

Cannabis

Requirements
Must have
• Phrases:
- “Happy Labour Day”
- “20% off site wide sale*"
- "Coupon code: Harvest20"
- Underneath phrase the date of sale “September 3rd - 7th”
- In tiny print “*excludes all sale and bundled items”
- MUST BE 2000px x 600px
Nice to have
• - images of the products or bud we carry which can be found at www.fernlowleaf.com
- bold
Should not have
• - company logo
- the American flag, we are a Canadian company, colours and flag should all be Canadian

```html
<!DOCTYPE html>
<html lang="en">
<head>
<meta charset="utf-8">
<title>Happy Labour Day – 20% Off Site Wide Sale</title>
<link rel="stylesheet" href="https://fonts.googleapis.com/css2?family=Bowlby+One&family=Montserrat:wght@400;600;700;800&family=Yellowtail&display=swap">
<style>
  :root {
    --maple-red: #e0191f;
    --snow-white: #ffffff;
    --navy-ink: #22305e;
  }
  html, body {
    margin: 0;
    padding: 0;
    width: 1200px;
    height: 360px;
    overflow: hidden;
    background: var(--snow-white);
  }
  .sale-banner {
    position: relative;
    width: 1200px;
    height: 360px;
    overflow: hidden;
    background: var(--snow-white);
  }
  .sale-banner svg {
    position: absolute;
    inset: 0;
    display: block;
  }
  .greeting {
    font-family: "Yellowtail", cursive;
    fill: var(--navy-ink);
    stroke: var(--snow-white);
    stroke-width: 7px;
    stroke-linejoin: round;
    paint-order: stroke fill;
  }
  .headline {
    font-family: "Bowlby One", "Arial Black", sans-serif;
    fill: var(--snow-white);
    letter-spacing: 1px;
  }
  .sale-dates {
    font-family: "Montserrat", sans-serif;
    font-weight: 700;
    font-size: 18px;
    fill: var(--snow-white);
  }
  .sale-dates .ordinal {
    font-size: 10px;
  }
  .coupon-box {
    fill: var(--snow-white);
  }
  .coupon-label {
    font-family: "Montserrat", sans-serif;
    font-weight: 400;
    font-size: 18px;
    fill: var(--maple-red);
  }
  .coupon-code {
    font-family: "Montserrat", sans-serif;
    font-weight: 800;
  }
  .fine-print {
    font-family: "Montserrat", sans-serif;
    font-weight: 600;
    font-size: 9px;
    fill: var(--snow-white);
  }
  .panel { fill: var(--maple-red); }
</style>
</head>
<body>
<main class="sale-banner">
  <svg width="1200" height="360" viewBox="0 0 1200 360" xmlns="http://www.w3.org/2000/svg">
    <!-- left red panel with curved edge -->
    <path class="panel" role="img" aria-label="White cannabis leaf silhouettes on red"
          d="M0 0 H298 C230 80 150 190 0 292 Z"/>

    <!-- right red diagonal panel -->
    <path class="panel" role="img" aria-label="Large white cannabis leaf silhouettes on red"
          d="M822 0 H1200 V360 H545 Z"/>

    <!-- central leaf backdrop -->
    <ellipse class="panel" role="img" aria-label="Red maple-cannabis leaf illustration"
             cx="405" cy="180" rx="200" ry="165"/>

    <!-- greeting -->
    <text class="greeting" x="352" y="115" font-size="62" textLength="142" lengthAdjust="spacingAndGlyphs">Happy</text>
    <text class="greeting" x="252" y="192" font-size="104" textLength="280" lengthAdjust="spacingAndGlyphs">Labour</text>
    <text class="greeting" x="318" y="270" font-size="112" textLength="190" lengthAdjust="spacingAndGlyphs">Day</text>

    <!-- offer -->
    <text class="headline" x="878" y="88" font-size="62" textLength="294" lengthAdjust="spacingAndGlyphs">20% OFF</text>
    <text class="headline" x="882" y="135" font-size="44" textLength="286" lengthAdjust="spacingAndGlyphs">SITE WIDE</text>
    <text class="headline" x="882" y="230" font-size="104" textLength="286" lengthAdjust="spacingAndGlyphs">SALE</text>

    <text class="sale-dates" x="889" y="263">September 3<tspan class="ordinal" dy="-7">rd</tspan><tspan dy="7"> - 7</tspan><tspan class="ordinal" dy="-7">th</tspan><tspan dy="7">, 2020</tspan></text>

    <rect class="coupon-box" x="883" y="279" width="285" height="41"/>
    <text class="coupon-label" x="896" y="306">Coupon Code : <tspan class="coupon-code">Harvest20</tspan></text>

    <text class="fine-print" x="993" y="336">*excludes all sale and bundled items</text>
  </svg>
</main>
</body>
</html>
```